Zorbent needs Brochure Design

we need a brochure design (4 A5 pages, first should be title page with creativity and last should be contact page. 2nd and 3rd should be more informative) for a new company based in Bern, Switzerland called zorbent. We are mobile solution company. We develop mobile apps for different smartphones. we use hybrid technology and browser based technology to develop the apps. we also develop for native platform like Qelpad. Secondly, we develop mobile website, thirdly, we consult company in mobilizing their business. for more details you can see our website www.zorbent-example.com
we would like to see the design which use the three color. two color would be same as the color or our logo, that is, orange and blue and other color could be light aluminium color.

The main message that we want to communicate is that Zorbent would help to the company to mobilize (developing apps, mobile website, mobile marketing, mobile strategy) their business to get the new generation customer. We are innovative, and technologically updates company and cost effective company. ( you can see the text from zorbent website)

The design should reflect a clear and complete message to our viewers.
Updates

Reason: I am travelling and have not enough time to look at design and giving me thoughts. Thank you for understanding.

Please check one design which I design one month before.. this will help to understand the content..

Reason: was delay in communication.. But I am active now and redy to finish this project this week

Reason: less time for feedback..

Reason: personal..

Target Market(s)

The target group is company CEO, Marketing managers of Small to medium size business

Industry/Entity Type

Business

Requirements
Must have
• The orange and blue color must match with the logo of the zorbent
clear and innovative look..
Nice to have
• place the QR code, a feeling of trust and professionalism
Should not have
• not to have too much content written.. not messy ..

```html
<!DOCTYPE html>
<html lang="en">
<head>
<meta charset="UTF-8">
<title>Zorbent – Brochure Spread</title>
<link href="https://fonts.googleapis.com/css2?family=Questrial&display=swap" rel="stylesheet">
<style>
  :root {
    --orange: #f7931e;
    --orange-soft: #fbd3aa;
    --blue: #0a6ab8;
    --aluminium: #d3d3d3;
    --panel: #f6f7f7;
    --ink: #1e1e1e;
    --white: #ffffff;
  }
  * { margin: 0; padding: 0; box-sizing: border-box; }
  html, body { width: 1200px; height: 855px; overflow: hidden; background: var(--white); }
  body { font-family: "Questrial", "Century Gothic", sans-serif; color: var(--ink); }

  .spread { position: relative; width: 1200px; height: 855px; overflow: hidden; background: var(--white); }

  /* Cover page */
  .cover { position: absolute; left: 0; top: 0; width: 600px; height: 855px; overflow: hidden; }
  .cover-field { position: absolute; left: 0; top: 0; width: 600px; height: 440px; background: var(--orange); }
  .cover-arcs { position: absolute; left: 0; top: 0; width: 600px; height: 855px; }
  .tile-band { position: absolute; left: 0; top: 440px; width: 600px; height: 120px; }
  .tile { position: absolute; background: var(--aluminium); }
  .brand { position: absolute; left: 64px; top: 468px; display: flex; align-items: center; gap: 14px; }
  .brand-mark { width: 34px; height: 34px; background: var(--orange); }
  .brand-name { font-size: 76px; line-height: 1; color: var(--ink); letter-spacing: 1px; }
  .tagline { position: absolute; left: 76px; top: 820px; font-size: 19px; color: var(--ink); }

  /* Inside page */
  .inside { position: absolute; left: 600px; top: 0; width: 600px; height: 855px; }
  .frame-bar { position: absolute; background: var(--blue); }
  .content-panel { position: absolute; left: 33px; top: 40px; width: 534px; height: 760px; background: var(--panel); }
  .section-title { position: absolute; left: 116px; top: 42px; font-size: 20px; color: var(--orange); font-weight: 400; }
  .intro-box {
    position: absolute; left: 103px; top: 83px; width: 466px; height: 266px;
    background: var(--orange); color: var(--white);
    padding: 10px 14px 0 14px; font-size: 12.4px; line-height: 1.35;
    box-shadow: 3px 5px 8px rgba(0,0,0,0.45);
  }
  .intro-box p { margin-bottom: 16px; }
  .visual-card { position: absolute; left: 140px; top: 377px; width: 409px; height: 403px; background: var(--white); border-radius: 6px; }
  .app-globe {
    position: absolute; left: 38px; top: 6px; width: 330px; height: 390px; border-radius: 50%;
    background: radial-gradient(circle at 45% 40%, #7ec8ef 0%, #e86a3a 35%, #8c4fb8 60%, #3aa655 80%, #d9402e 100%);
  }
</style>
</head>
<body>
<main class="spread">

  <section class="cover">
    <div class="cover-field"></div>
    <svg class="cover-arcs" viewBox="0 0 600 855" aria-hidden="true">
      <path d="M 70 855 C 60 480, 260 120, 600 70" fill="none" stroke="rgba(253,226,196,0.45)" stroke-width="110"/>
      <path d="M 200 440 C 250 270, 400 160, 600 150" fill="none" stroke="rgba(253,226,196,0.3)" stroke-width="36"/>
    </svg>
    <div class="tile-band" aria-hidden="true">
      <div class="tile" style="left:0;top:0;width:148px;height:56px"></div>
      <div class="tile" style="left:160px;top:0;width:136px;height:56px"></div>
      <div class="tile" style="left:307px;top:0;width:140px;height:56px"></div>
      <div class="tile" style="left:460px;top:0;width:140px;height:56px"></div>
      <div class="tile" style="left:0;top:64px;width:148px;height:56px"></div>
      <div class="tile" style="left:160px;top:64px;width:136px;height:56px"></div>
      <div class="tile" style="left:307px;top:64px;width:140px;height:56px"></div>
      <div class="tile" style="left:460px;top:64px;width:140px;height:56px"></div>
    </div>
    <div class="brand">
      <span class="brand-mark" aria-hidden="true"></span>
      <span class="brand-name">Zorbent</span>
    </div>
    <p class="tagline">The Mobile Solution Company</p>
  </section>

  <section class="inside">
    <div class="content-panel"></div>
    <div class="frame-bar" style="left:273px;top:4px;width:314px;height:13px"></div>
    <div class="frame-bar" style="left:574px;top:4px;width:13px;height:64px"></div>
    <div class="frame-bar" style="left:7px;top:273px;width:20px;height:582px"></div>
    <div class="frame-bar" style="left:7px;top:833px;width:493px;height:20px"></div>

    <h2 class="section-title">What We Do</h2>
    <div class="intro-box">
      <p>At Zorbent our goal is to help your business deliver a big impact on the mobile screen. We offer best-of-breed solutions for organizations looking to take full advantage of all the mobilized business opportunities available today and tomorrow.</p>
      <p>Our expertise enables us to implement cost-effective and technologically sound solutions for your business the first time.<br>We will take your business mobile.</p>
      <p>We offer the latest available technology in Mobile App Development, Mobile Website, M-Commerce, and Mobile Consulting Services for a wide range of industries and business areas.</p>
      <p>Zorbent specialists will help take your business mobile.</p>
    </div>
    <div class="visual-card">
      <div class="app-globe" role="img" aria-label="Globe made of colourful mobile app icons"></div>
    </div>
  </section>

</main>
</body>
</html>
```